Kestrel Ridge Partners LLC
Business card and stationary set for Investment Firm - Financial Services
Business card and stationary set for Investment Firm
Simple
Owen Talcott
President / Founder
4820 Birchwood Lane Sparta, IL 62286
owen@talcottwealth.example
www.talcottwealth.example
jdalvin jdalvin
Also, please keep a simple, prestigious / exclusive look to the design.
Designers- I am looking for a design that uses watermarks and different parts of the logo separated out to create some originality. I only want to see the the "Professional Investment Management" one time in the design with the logo. Also, there are 2 formats of the logo in the files I uploaded. One has the graphic on the side and the other on the top. I'd like to see the use of both of these. I do like the blue on the back of the card...maybe a watermark included. The most creative will probably get the win on this. Thank you.
bluequill bluequill
Can u do some sort of star rating, which help us to make these changes,and then i will submit you stationary package with your requirements.. thanks
Also, thank you cards.
Designers - A few things I'll need in the design will be the removal of "Professional Investment Management" from the logo on the front of the card. I still like it to be on the back OR on the larger logo. I only wanted it listed on one of the logos as opposed to both of them. Also, I do like the look and feel of an exclusive, simple, unique design. I do like the back side of the card to be the blue color. I like a background image of the logo as well to add texture. Finally, I need a full stationary design including letterhead, envelopes and return of all sizes (standard and 10X 13), business cards, folders and 1/4 page paper pad. Thank you.
Vandal Vandal
Star Rating please....
Also, please include simple envelope design
Be sure to include standard stationary design as well. The font does not need to be the same as the logo on all pieces.
Designers - Feel free to remove the tagline "Professional Investment Management" in parts of the stationary and business cards. It can be included but isn't necessary. Thank you.

```html
<!DOCTYPE html>
<html lang="en">
<head>
<meta charset="utf-8">
<title>Kestrel Ridge Partners LLC — Business Cards</title>
<link rel="stylesheet" href="https://fonts.googleapis.com/css2?family=Open+Sans:wght@400;600&display=swap">
<style>
  :root {
    --bg: #6f7173;
    --card-white: #ffffff;
    --brand-teal: #1f5f78;
    --panel-grey: #a7a9ac;
    --text-grey: #8a8d90;
    --text-light: #e6eef2;
    --shadow: 0 14px 28px rgba(0,0,0,0.35);
  }
  * { box-sizing: border-box; margin: 0; padding: 0; }
  html, body { width: 1200px; height: 908px; overflow: hidden; }
  body {
    background: var(--bg);
    font-family: "Open Sans", Arial, sans-serif;
    position: relative;
  }
  .card {
    position: absolute;
    width: 560px;
    height: 320px;
    border-radius: 22px;
    overflow: hidden;
    box-shadow: var(--shadow);
  }

  /* Front */
  .card-front {
    left: 90px; top: 90px;
    background: var(--card-white);
    display: flex; flex-direction: column; align-items: center; justify-content: center;
  }
  .brand {
    display: flex; align-items: center; gap: 14px;
    color: var(--brand-teal);
    font-weight: 600;
    text-transform: uppercase;
    letter-spacing: 1px;
    white-space: nowrap;
  }
  .brand-mark { background: var(--brand-teal); flex: none; }
  .card-front .brand { font-size: 25px; }
  .card-front .brand-mark { width: 34px; height: 34px; }
  .front-web {
    margin-top: 26px;
    font-size: 16px;
    color: var(--text-grey);
    letter-spacing: 0.5px;
  }

  /* Back */
  .card-back {
    left: 550px; top: 500px;
    background: var(--panel-grey);
  }
  .back-info {
    position: absolute; right: 0; top: 0;
    width: 258px; height: 210px;
    background: var(--brand-teal);
    padding: 30px 16px 0 26px;
    color: var(--text-light);
  }
  .person-name { font-size: 21px; font-weight: 600; color: #fff; }
  .person-title { font-size: 12.5px; margin-top: 2px; }
  .contact-list { list-style: none; margin-top: 18px; font-size: 12px; line-height: 1.55; }
  .contact-list li { display: flex; align-items: flex-start; gap: 8px; }
  .contact-list svg { width: 11px; height: 11px; flex: none; margin-top: 4px; fill: var(--text-light); }
  .back-logo-panel {
    position: absolute; left: 30px; top: 70px;
    width: 254px; height: 220px;
    background: var(--card-white);
    border-radius: 18px;
    display: flex; align-items: center; justify-content: center;
  }
  .back-logo-panel .brand {
    flex-direction: column; gap: 12px;
    font-size: 12px; letter-spacing: 0.8px;
  }
  .back-logo-panel .brand-mark { width: 40px; height: 40px; }
</style>
</head>
<body>
  <section class="card card-front" aria-label="Business card front">
    <div class="brand"><span class="brand-mark"></span>Kestrel Ridge Partners LLC</div>
    <p class="front-web">www.talcottwealth.example</p>
  </section>

  <section class="card card-back" aria-label="Business card back">
    <div class="back-info">
      <p class="person-name">Owen Talcott</p>
      <p class="person-title">President / Founder</p>
      <ul class="contact-list">
        <li><svg viewBox="0 0 12 12"><path d="M6 0a4 4 0 0 0-4 4c0 3 4 8 4 8s4-5 4-8a4 4 0 0 0-4-4zm0 5.5A1.5 1.5 0 1 1 6 2.5a1.5 1.5 0 0 1 0 3z"/></svg><span>4820 Birchwood Lane<br>Sparta, IL 62286</span></li>
        <li><svg viewBox="0 0 12 12"><path d="M2.5 0.5l2 2-1 1.5a7 7 0 0 0 4.5 4.5l1.5-1 2 2-1.5 2C5 11.5 0.5 7 0.5 2z"/></svg><span>(618) 555-0142</span></li>
        <li><svg viewBox="0 0 12 12"><path d="M0 2h12v8H0zm1 1v.4l5 3.3 5-3.3V3z"/></svg><span>owen@talcottwealth.example</span></li>
        <li><svg viewBox="0 0 12 12"><circle cx="6" cy="6" r="5.5"/></svg><span>www.talcottwealth.example</span></li>
      </ul>
    </div>
    <div class="back-logo-panel">
      <div class="brand"><span class="brand-mark"></span>Kestrel Ridge Partners LLC</div>
    </div>
  </section>
</body>
</html>
```